A professional business to business web site for a contract agency called VANTOMER.

We need a very clean, very professional web site created for business to business. It is an informational web site with 3 pages. We are a company that offers contract employee placements into primarily the pharmaceutical industry. I have attached a file that describes the company more fully.
Updates

Hi,

I'm sorry if I wasn't clear, but I need to have the HTML pages created so I can just upload the files you give me to the web hosting site.

Please let me know if you have any questions.

Thanks for working on my project!

Hello,

I didn't put this in the description, but I would need the web site set up on the web hosting site as well.  The web hosting site is bluepinecrest.  I want a copy of all the files as well.

Thanks,
Milo

Reason: I'm sorry, unexpectedly, I have been very busy and I haven't been able to devote the time necessary for this. I am extending the deadline by 10 days. Thank you for your patience. Thanks.

Reason: Hi everyone, I apologize again, but everything has been so busy here that I haven't been able to give this attention. I plan to work on this over the next few days. Thanks and sorry again, Milo.

Reason: I'm sorry this is taking longer than planned. I have been extremely busy. I have increased the budget on this project. Thanks.

Target Market(s)

Large professional corporations mainly in the pharmaceutical industry. The audience is hiring decisions makers within the companies and potential job candidates/job seekers.

Industry/Entity Type

Pharmaceutical

Font styles to use
Sans Serif

Requirements
Must have
• Must have a clean look that mimics the pharmaceutical industry web sites. VERY professional.
Nice to have
• A nice picture of professional business/pharma/technical people looking like a team. Colors are listed on the attached Word document.
Should not have
• No animation. Not too busy.

```html
<!DOCTYPE html>
<html lang="en">
<head>
<meta charset="utf-8">
<title>VANTOMER – Services</title>
<link href="https://fonts.googleapis.com/css2?family=Arimo:wght@400;700&display=swap" rel="stylesheet">
<style>
:root{
  --navy:#1d2680;
  --text:#6f6f6f;
  --dark-text:#444;
  --rule:#dcdcdc;
  --footer:#343434;
  --footer-bottom:#1f1f1f;
  --footer-text:#c9c9c9;
  --footer-muted:#8d8d8d;
  --link:#3aa0e0;
  --photo-a:#b5c8cc;
  --photo-b:#52707a;
}
*{margin:0;padding:0;box-sizing:border-box}
html,body{width:1200px;height:1091px;overflow:hidden;background:#fff}
body{font-family:"Arimo",Arial,sans-serif;color:var(--text)}
.page{position:relative;width:1100px;height:1000px;transform:scale(1.090909);transform-origin:0 0}
.abs{position:absolute}
.hotline{right:219px;top:6px;font-size:7.5px;color:#777}
.brand{left:237px;top:32px;display:flex;align-items:center;gap:10px}
.brand-dot{width:30px;height:30px;border-radius:50%;background:var(--navy)}
.brand-name{font-size:16px;letter-spacing:3px;color:var(--navy)}
.nav{left:583px;top:45px;display:flex;font-size:7.2px;color:#555}
.nav a{padding:0 8px;border-left:1px solid var(--rule);color:inherit;text-decoration:none;line-height:9px;position:relative}
.nav a:first-child{border-left:0}
.nav a.active{color:var(--navy)}
.nav a.active::after{content:"";position:absolute;left:6px;right:5px;top:19px;height:3px;background:var(--navy)}
.search{left:871px;top:44px}
.hr{left:0;width:1100px;height:1px;background:var(--rule)}
.page-title{left:238px;top:78px;font-size:10px;color:#777;letter-spacing:.5px}
.crumbs{right:219px;top:79px;font-size:7.2px;color:#888}
.main{left:238px;width:400px;font-size:7.2px;line-height:10px}
.h{font-size:7.6px;color:#333;text-transform:uppercase}
.divider{height:6px;position:relative}
.divider::before{content:"";position:absolute;left:0;top:0;width:5px;height:5px;border-radius:50%;background:#ccc}
.divider::after{content:"";position:absolute;left:12px;right:0;top:2px;height:1px;background:var(--rule)}
.btn{display:inline-flex;align-items:center;gap:8px;width:74px;height:24px;border:1px solid #d6d6d6;padding-left:9px;font-size:7.2px;color:#888}
.btn i{width:9px;height:9px;border:1px solid #999;border-radius:50%;font-style:normal;font-size:6px;display:flex;align-items:center;justify-content:center;color:#999}
.photo{background:linear-gradient(160deg,var(--photo-a),var(--photo-b))}
.vline{left:669px;top:128px;width:1px;height:449px;background:var(--rule)}
.side-menu{left:690px;top:128px;width:118px;font-size:7.2px;font-weight:700;color:#555}
.side-menu li{list-style:none;border-bottom:1px solid var(--rule);height:34px;display:flex;align-items:center;line-height:9px}
.side-menu li.current{color:var(--navy)}
.footer{left:0;top:795px;width:1100px;height:169px;background:var(--footer)}
.footer-bottom{left:0;top:964px;width:1100px;height:36px;background:var(--footer-bottom);font-size:6.8px;color:var(--footer-muted)}
.f-h{font-size:7.6px;color:#e6e6e6;padding-bottom:6px;border-bottom:1px solid #555;width:110px}
.f-text{font-size:6.6px;line-height:10px;color:var(--footer-muted);font-style:italic}
.f-info{font-size:6.8px;line-height:13px;color:var(--footer-text)}
.social{display:flex;gap:5px}
.social span{width:16px;height:16px;border-radius:50%;background:#9a9a9a}
.bottom-links a{color:#ddd;text-decoration:none;padding:0 4px;border-left:1px solid #777}
.bottom-links a:first-child{border-left:0}
</style>
</head>
<body>
<div class="page">
  <div class="abs hotline">Hotline Support - <span style="color:#555">555-214-0388</span></div>
  <div class="abs brand"><span class="brand-dot"></span><span class="brand-name">VANTOMER</span></div>
  <nav class="abs nav">
    <a href="#">HOME</a><a href="#" class="active">SERVICES</a><a href="#">TEAM</a><a href="#">FEATURES</a><a href="#">BLOG</a><a href="#">CONTACT US</a>
  </nav>
  <svg class="abs search" width="11" height="11" viewBox="0 0 11 11"><circle cx="4.5" cy="4.5" r="3.3" fill="none" stroke="#aaa" stroke-width="1"/><line x1="7" y1="7" x2="10" y2="10" stroke="#aaa" stroke-width="1.2"/></svg>
  <div class="abs hr" style="top:67px"></div>
  <div class="abs page-title">SERVICES</div>
  <div class="abs crumbs">You are here: Home/Services</div>
  <div class="abs hr" style="top:98px"></div>

  <section class="abs main" style="top:125px">
    <div class="h">VANTOMER Features</div>
    <div class="divider" style="margin-top:8px"></div>
    <p style="margin-top:11px">VANTOMERspecializes in offering contract professionals primarily to companies in pharmaceutical lab environments.&nbsp; We look for the top people and companies to work with.&nbsp; Whether you are looking for a position, or looking for a contractor, you have come to the right place.</p>
    <ol style="list-style:none;margin-top:17px;line-height:8.5px">
      <li>&nbsp;a.&nbsp;&nbsp;&nbsp;&nbsp;&nbsp;&nbsp;Project Managers</li>
      <li>&nbsp;b.&nbsp;&nbsp;&nbsp;&nbsp;&nbsp;&nbsp;Chromatography instrument and sotware training.</li>
      <li>&nbsp;c.&nbsp;&nbsp;&nbsp;&nbsp;&nbsp;&nbsp;Laboratory technicians</li>
    </ol>
    <div style="margin-top:23px"><span class="btn"><i>i</i>Learn More</span></div>
  </section>

  <div class="abs main divider" style="top:291px"></div>
  <div class="abs photo" style="left:239px;top:305px;width:194px;height:97px" role="img" aria-label="Businessman in a suit holding an umbrella and an orange folder"></div>
  <div class="abs photo" style="left:443px;top:305px;width:194px;height:97px" role="img" aria-label="Businessman in a suit holding an umbrella and an orange folder"></div>
  <p class="abs main" style="top:411px;width:190px">VANTOMERspecializes in offering contract professionals primarily to companies in pharmaceutical lab environments. We look for the top people and companies to work with. Whether you are looking for a position, or looking for a con-tractor, you have come to the right place.</p>
  <p class="abs main" style="left:443px;top:411px;width:194px">VANTOMERspecializes in offering contract professionals primarily to companies in pharmaceutical lab environments. We look for the top people and companies to work with.</p>
  <span class="abs btn" style="left:238px;top:474px">  <i>i</i>Learn More</span>
  <span class="abs btn" style="left:443px;top:474px"><i>i</i>Learn More</span>

  <div class="abs main divider" style="top:522px"></div>
  <div class="abs h" style="left:238px;top:547px">Heading goes here</div>
  <div class="abs photo" style="left:239px;top:568px;width:126px;height:80px" role="img" aria-label="Businessman holding an umbrella and an orange folder"></div>
  <p class="abs main" style="left:375px;top:567px;width:265px">VANTOMERspecializes in offering contract professionals primarily to companies in pharmaceutical lab environments.&nbsp; We look for the top people and companies to work with.&nbsp; Whether you are looking for a position, or looking for a contractor, you have come to the right place.</p>
  <span class="abs btn" style="left:375px;top:626px"><i>i</i>Learn More</span>

  <div class="abs h" style="left:238px;top:666px">Heading goes here</div>
  <div class="abs photo" style="left:239px;top:687px;width:126px;height:80px" role="img" aria-label="Businessman holding an umbrella and an orange folder"></div>
  <p class="abs main" style="left:375px;top:686px;width:265px">VANTOMERspecializes in offering contract professionals primarily to companies in pharmaceutical lab environments.&nbsp; We look for the top people and companies to work with.&nbsp; Whether you are looking for a position, or looking for a contractor, you have come to the right place.</p>
  <span class="abs btn" style="left:375px;top:745px"><i>i</i>Learn More</span>

  <div class="abs vline"></div>
  <ul class="abs side-menu">
    <li class="current">Overall VANTOMER</li>
    <li>Chromatography instrument and sotware training.</li>
    <li>Laboratory technicians</li>
    <li>Project Managers</li>
  </ul>
  <div class="abs photo" style="left:690px;top:290px;width:192px;height:80px" role="img" aria-label="Businessmen in suits holding umbrellas"></div>
  <div class="abs h" style="left:690px;top:381px">Heading goes here</div>
  <p class="abs main" style="left:690px;top:399px;width:195px">VANTOMERspecializes in offering contract professionals primarily to companies in pharmaceutical lab environments.</p>
  <span class="abs btn" style="left:690px;top:430px"><i>i</i>Learn More</span>

  <footer class="abs footer">
    <div class="abs" style="left:240px;top:32px;width:36px;height:36px;border-radius:50%;background:#5a5a5a"></div>
    <div class="abs f-h" style="left:290px;top:42px">ABOUT VANTOMER</div>
    <p class="abs f-text" style="left:237px;top:72px;width:270px">Lorem Ipsum is simply dummy text of the printing and typesetting industry. Lorem Ipsum has been the industry's standard dummy text ever since the 1500s, when an unknown printer took a galley of type and scrambled it to make a type specimen book.</p>
    <p class="abs f-text" style="left:237px;top:110px;width:270px">Lorem Ipsum is simply dummy text of the printing and typesetting industry. Lorem Ipsum has been the industry's standard dummy text ever since the 1500s, when an unknown printer took</p>
    <div class="abs f-h" style="left:560px;top:42px">OFFICE LOCATION</div>
    <div class="abs f-info" style="left:560px;top:71px">
      1480 Harbor Crest Way, Oceanside, CA 92054<br>
      Email: <span style="color:var(--link);text-decoration:underline">contact.us@VANTOMER.com</span><br>
      Call: <b style="color:#fff;font-size:8px">555-214-0388</b>
    </div>
    <div class="abs f-h" style="left:772px;top:42px;width:109px">SOCIAL LINKS</div>
    <div class="abs social" style="left:772px;top:72px"><span></span><span></span><span></span><span></span></div>
  </footer>
  <div class="abs footer-bottom">
    <div class="abs" style="left:240px;top:16px">All right reserved 2014.</div>
    <div class="abs bottom-links" style="right:215px;top:16px"><a href="#">Home</a><a href="#">Services</a><a href="#">Team</a><a href="#">Features</a><a href="#">Blogs</a><a href="#">Contact Us</a></div>
  </div>
</div>
</body>
</html>
```